****Amazing Solar Energy Company | Needs A Dynamic Website In Wordpress ****

Here at Brivane Solar, our approach is straightforward: we listen, educate, and collaborate. We are a Residential & Commercial solar energy company located in Sanford, FL. OLD TEMP Website https://www.brivanesolar-example.com/

We are looking for a dynamic website design, layout, and code in Wordpress. We will be using a builder (Elementor) post-install so keep that in mind.

IMPORTANT:
Please See brand kit, font type, site map, and even a rough home page. We even have persona targets if needed.

Please review all images and documents uploaded as well

Please rely on your own design with the goal to educate the consumer on the many benefits of solar energy.

Target Market(s)

Home Owners who are looking for Solar Panels

Industry/Entity Type

Solar Energy, Solar Panels, Green Energy

Coding

Coded - Design and coding required

Number of Pages Required

5+ page

Font styles to use
Other font styles liked:
• Header: Raleway Body Text: Montserrat

Colors

Designer to choose colors to be used in the design.

Requirements
Must have
• Must follow the brand kit color, fonts etc | Must be clean and engaging | Modern, Simplistic, Impact, Clean, Cooling, Calming
Nice to have
• Rotating Header, Step By Steps Visuals

```html
<!DOCTYPE html>
<html lang="en">
<head>
<meta charset="utf-8">
<title>Brivane Solar — Building Bright Partnerships</title>
<link href="https://fonts.googleapis.com/css2?family=Raleway:wght@500;600;700;800&family=Arimo:wght@400;700&display=swap" rel="stylesheet">
<style>
:root{
  --teal:#2b8c7e;
  --teal-light:#36a08f;
  --teal-dark:#1f6f66;
  --navy:#213f4b;
  --navy-deep:#1b3540;
  --gold:#e3b94c;
  --red:#d9473a;
  --text:#555b5f;
  --heading:#243e4a;
  --white:#ffffff;
}
*{box-sizing:border-box;margin:0;padding:0}
html,body{width:1200px;height:4644px;overflow:hidden;background:var(--white)}
body{position:relative;font-family:"Arimo",Arial,sans-serif;color:var(--text)}
.abs{position:absolute}
.btn{position:absolute;display:flex;align-items:center;justify-content:center;gap:8px;border-radius:40px;font-family:"Raleway",sans-serif;font-weight:700;font-size:15px;color:var(--white);letter-spacing:.3px}

/* header */
.brand{position:absolute;display:flex;align-items:center;gap:10px;font-family:"Raleway",sans-serif;font-weight:700;color:var(--heading)}
.brand-dot{border-radius:50%;background:var(--gold)}
.social{position:absolute;top:22px;left:569px;display:flex;gap:7px}
.social span{width:35px;height:35px;border:2px solid var(--navy);border-radius:50%}
.callus{position:absolute;top:30px;left:745px;display:flex;align-items:center;gap:10px;font-family:"Raleway",sans-serif;font-weight:700;font-size:14px;color:var(--heading)}
.nav{position:absolute;top:86px;left:0;width:1200px;font-family:"Raleway",sans-serif;font-weight:700;font-size:14px;color:var(--heading)}
.nav a{position:absolute;text-decoration:none;color:inherit}
.nav a.active{color:var(--teal)}

/* hero */
.hero-photo{position:absolute;top:121px;left:0;width:1200px;height:726px;background:linear-gradient(160deg,#b9cbd9 0%,#8aa6c0 35%,#3a68a3 62%,#23477d 100%)}
.hero-title{position:absolute;top:385px;left:76px;font-family:"Raleway",sans-serif;font-weight:700;font-size:46px;color:var(--white)}
.hero-sub{position:absolute;top:452px;left:76px;font-family:"Raleway",sans-serif;font-weight:700;font-size:26px;color:var(--white)}
.dots{position:absolute;top:806px;left:733px;display:flex;gap:9px}
.dots span{width:12px;height:12px;border-radius:50%;background:#fff}
.dots span+span{background:#dfe7ea}

/* welcome */
.welcome-kicker{position:absolute;top:920px;left:0;width:1200px;text-align:center;font-family:"Raleway",sans-serif;font-weight:600;font-size:19px;color:var(--heading)}
.welcome-title{position:absolute;top:944px;left:0;width:1200px;text-align:center;font-family:"Raleway",sans-serif;font-weight:700;font-size:36px;color:var(--teal)}
.welcome-copy{position:absolute;top:1016px;left:270px;width:660px;text-align:center;font-size:14.5px;line-height:28px}
.welcome-copy p+p{margin-top:28px}

/* feature cards */
.card{position:absolute;top:1389px;width:306px;height:258px;border-radius:6px;text-align:center}
.card .disc{width:133px;height:133px;border-radius:50%;background:#fff;margin:22px auto 0;display:flex;align-items:center;justify-content:center}
.card h3{font-family:"Raleway",sans-serif;font-weight:700;font-size:17px;line-height:28px;color:#fff;margin-top:30px}

/* split */
.split-text h2{font-family:"Raleway",sans-serif;font-weight:700;font-size:34px;color:#fff}
.split-text p{font-size:15px;line-height:27px;color:#fff;margin-top:18px}
.btn-outline{border:3px solid #fff}

/* benefits */
.benefit h4{font-family:"Raleway",sans-serif;font-weight:700;font-size:17px;color:var(--heading)}
.benefit p{font-size:13px;line-height:26px;margin-top:6px}
.benefit.left{text-align:right}

/* about */
.about-title{position:absolute;top:3072px;left:650px;font-family:"Raleway",sans-serif;font-weight:700;font-size:40px;color:#fff}
.about-rule{position:absolute;top:3128px;left:650px;width:56px;height:3px;background:#fff}
.about-copy{position:absolute;top:3150px;left:650px;width:424px;font-size:13px;line-height:25.8px;color:#fff;text-align:justify}
.about-copy p+p{margin-top:25px}

/* blog */
.section-title{position:absolute;left:0;width:1200px;text-align:center;font-family:"Raleway",sans-serif;font-weight:700;font-size:36px;color:var(--heading)}
.section-title em{font-style:normal;color:var(--teal)}
.blog-card{position:absolute;top:3706px;width:311px}
.blog-img{height:252px;width:100%}
.blog-date{margin:-22px 16px 0;background:#fff;position:relative;text-align:center;padding-top:14px;font-family:"Raleway",sans-serif;font-weight:700;font-size:18px;color:var(--teal)}
.blog-card h3{text-align:center;font-family:"Raleway",sans-serif;font-weight:700;font-size:16px;line-height:23px;color:var(--heading);margin-top:12px}
.blog-card p{text-align:center;font-size:12.5px;line-height:25px;margin:10px 22px 0}

/* footer */
.footer-head{position:absolute;top:4285px;font-family:"Raleway",sans-serif;font-weight:700;font-size:20px;color:#fff}
.footer-about{position:absolute;top:4365px;left:112px;width:242px;font-size:12.5px;line-height:26px;color:#fff;text-align:justify}
.contact-item{position:absolute;left:389px;color:#fff}
.contact-item h5{font-family:"Raleway",sans-serif;font-weight:700;font-size:15px;margin-left:40px}
.contact-item p{font-size:12.5px;line-height:23px;margin-left:40px}
.contact-item svg{position:absolute;left:0;top:2px}
.post{position:absolute;left:629px;display:flex;gap:20px;color:#fff}
.post .thumb{width:86px;height:74px}
.post p{font-size:13px;margin-top:12px}
.post small{display:flex;align-items:center;gap:6px;font-size:13px;margin-top:12px}
.work{position:absolute;width:85px;height:84px}
.copyright{position:absolute;top:4592px;left:0;width:1200px;text-align:center;font-size:16px;color:#fff}
</style>
</head>
<body>

<header>
  <div class="brand" style="top:42px;left:112px;font-size:32px;">
    <span class="brand-dot" style="width:22px;height:22px;"></span>Brivane Solar
  </div>
  <div class="social" aria-label="Social links"><span></span><span></span><span></span><span></span></div>
  <div class="callus">
    <svg width="20" height="20" viewBox="0 0 24 24" fill="none" stroke="#2b8c7e" stroke-width="2"><path d="M5 3h4l2 5-2.5 1.5a11 11 0 0 0 6 6L16 13l5 2v4a2 2 0 0 1-2 2A17 17 0 0 1 3 5a2 2 0 0 1 2-2z"/></svg>
    CALL US : (555.014.2290)
  </div>
  <div class="btn" style="top:20px;left:978px;width:110px;height:41px;background:var(--teal);font-size:14px;">
    <svg width="16" height="16" viewBox="0 0 24 24" fill="none" stroke="#fff" stroke-width="2"><circle cx="12" cy="12" r="10"/><circle cx="12" cy="10" r="3"/><path d="M6 19c2-3 10-3 12 0"/></svg>LOGIN
  </div>
  <nav class="nav">
    <a class="active" style="left:495px">HOME</a>
    <a style="left:578px">OUR COMPANY</a>
    <a style="left:726px">SERVICES</a>
    <a style="left:834px">REVIEWS</a>
    <a style="left:940px">BLOG</a>
    <a style="left:1021px">CONTACT</a>
  </nav>
</header>

<section>
  <div class="hero-photo" role="img" aria-label="Installer in blue coveralls and white hard hat fitting solar panels on a roof under a winter sky"></div>
  <svg class="abs" style="top:121px;left:0" width="1200" height="726" viewBox="0 0 1200 726">
    <polygon points="0,171 486,171 625,497 0,497" fill="#2b8c7e" opacity=".92"/>
    <polygon points="0,645 775,720 1200,645 1200,726 0,726" fill="#2b8c7e"/>
    <polygon points="0,660 775,726 1200,660 1200,726 0,726" fill="#fff"/>
  </svg>
  <div class="hero-title">BRIVANE SOLAR</div>
  <div class="hero-sub">BUILDING BRIGHT PARTNERSHIPS</div>
  <div class="btn" style="top:512px;left:76px;width:182px;height:54px;background:var(--teal-light);">READ MORE</div>
  <div class="dots"><span></span><span></span><span></span></div>
</section>

<section>
  <div class="welcome-kicker">WELCOME TO</div>
  <h1 class="welcome-title">BRIVANE SOLAR</h1>
  <div class="welcome-copy">
    <p>Brivane: a derivative of the Latin word Socius (noun); partner, ally At Brivane Solar, we believe that solid partnerships are the building blocks behind every success story. By approaching every aspect of our business model with transparency and integrity, we have built a foundation of industry-leading experts and lifelong clients.</p>
    <p>Our approach is simple: we listen, educate and collaborate. Brivane is dedicated to offering our partners the highest-level of non-bias industry education so they are empowered to make the right decision based on their needs, not ours.</p>
  </div>
  <div class="btn" style="top:1276px;left:511px;width:178px;height:57px;background:linear-gradient(90deg,var(--teal),var(--navy));">LEARN MORE</div>

  <div class="card" style="left:112px;background:var(--teal);">
    <div class="disc"><svg width="62" height="62" viewBox="0 0 24 24" fill="none" stroke="#2b8c7e" stroke-width="1.4"><rect x="3" y="3" width="18" height="18" stroke-dasharray="2 2"/><rect x="3" y="13" width="8" height="8"/><path d="M19 5l-6 6M13 7v4h4"/></svg></div>
    <h3>REDUCE / ELIMINATE<br>UTILITY BILLS</h3>
  </div>
  <div class="card" style="left:447px;background:linear-gradient(150deg,#e4c160,#cfa53a);">
    <div class="disc"><svg width="62" height="62" viewBox="0 0 24 24" fill="none" stroke="#d2a63c" stroke-width="1.4"><path d="M12 3c3 2 3 7 0 9-3-2-3-7 0-9zM12 6v9"/><path d="M3 10v6l4 5h3v-4l-3-3M21 10v6l-4 5h-3v-4l3-3"/></svg></div>
    <h3>PROTECT THE<br>ENVIRONMENT</h3>
  </div>
  <div class="card" style="left:782px;background:var(--red);">
    <div class="disc"><svg width="62" height="62" viewBox="0 0 24 24" fill="none" stroke="#d9473a" stroke-width="1.4"><path d="M3 11l9-8 9 8M5 9v12h9M10 21v-6h4"/><circle cx="17" cy="15" r="3"/><path d="M17 18l-2 3M17 18l2 3"/></svg></div>
    <h3>INCREASE PROPERTY<br>VALUE</h3>
  </div>
</section>

<section>
  <svg class="abs" style="top:1676px;left:0" width="1200" height="675" viewBox="0 0 1200 675" role="img" aria-label="Solar panel installations on residential and commercial roofs, tinted teal and navy">
    <rect x="0" y="0" width="600" height="675" fill="#2b8a7c"/>
    <rect x="600" y="0" width="600" height="675" fill="#233f4b"/>
    <polygon points="0,0 1200,0 600,130" fill="#fff"/>
    <polyline points="380,88 600,130 820,88" fill="none" stroke="#e3b94c" stroke-width="6"/>
    <polygon points="0,675 600,555 1200,675" fill="#fff"/>
    <polyline points="380,600 600,555 820,600" fill="none" stroke="#e3b94c" stroke-width="6"/>
  </svg>
  <div class="split-text abs" style="top:1895px;left:84px;width:360px;">
    <h2>RESIDENTIAL SOLAR</h2>
    <p>Take power into your own hands by booking an educational consultation to learn more about the residential solar industry.</p>
  </div>
  <div class="btn btn-outline" style="top:2081px;left:90px;width:189px;height:54px;">READ MORE
    <svg width="16" height="16" viewBox="0 0 24 24"><circle cx="12" cy="12" r="11" fill="#fff"/><path d="M9 7l5 5-5 5" stroke="#2b8a7c" stroke-width="3" fill="none"/></svg></div>
  <div class="split-text abs" style="top:1895px;left:744px;width:380px;text-align:right;">
    <h2>COMMERCIAL SOLAR</h2>
    <p>Take your business to the next level by booking an educational consultation to learn more about the commercial solar industry.</p>
  </div>
  <div class="btn btn-outline" style="top:2081px;left:928px;width:191px;height:54px;">READ MORE
    <svg width="16" height="16" viewBox="0 0 24 24"><circle cx="12" cy="12" r="11" fill="#fff"/><path d="M9 7l5 5-5 5" stroke="#233f4b" stroke-width="3" fill="none"/></svg></div>
</section>

<section>
  <h2 class="section-title" style="top:2350px;">BENEFITS <em>OF SOLAR</em></h2>
  <svg class="abs" style="top:2421px;left:340px" width="520" height="520" viewBox="0 0 520 520">
    <circle cx="260" cy="260" r="230" fill="none" stroke="#243e4a" stroke-width="2" stroke-dasharray="6 5"/>
    <circle cx="260" cy="260" r="157" fill="#223e49"/>
    <g>
      <circle cx="100" cy="96" r="31" fill="#d9473a"/>
      <path d="M86 110h28M90 110V94h6v16M100 110V86h6v24M110 110v-12" stroke="#fff" stroke-width="2" fill="none"/>
      <circle cx="44" cy="235" r="31" fill="#e3b94c"/>
      <circle cx="44" cy="235" r="14" stroke="#fff" stroke-width="2" fill="none"/>
      <path d="M46 224l-6 12h8l-6 12" stroke="#fff" stroke-width="2" fill="none"/>
      <circle cx="82" cy="401" r="31" fill="#d9473a"/>
      <path d="M70 389l24 24M94 389l-24 24" stroke="#fff" stroke-width="3"/>
      <circle cx="408" cy="96" r="31" fill="#d9473a"/>
      <circle cx="408" cy="96" r="15" stroke="#fff" stroke-width="2" fill="none"/>
      <path d="M408 86c5 4 5 12 0 16-5-4-5-12 0-16z" stroke="#fff" stroke-width="2" fill="none"/>
      <circle cx="474" cy="235" r="31" fill="#e3b94c"/>
      <circle cx="474" cy="229" r="9" stroke="#fff" stroke-width="2" fill="none"/>
      <path d="M460 240v8l8 4M488 240v8l-8 4" stroke="#fff" stroke-width="2" fill="none"/>
      <circle cx="447" cy="399" r="31" fill="#d9473a"/>
      <path d="M433 397l14-12 14 12M437 394v16h20v-16" stroke="#fff" stroke-width="2" fill="none"/>
    </g>
    <text x="260" y="268" text-anchor="middle" font-family="Raleway, sans-serif" font-weight="700" font-size="30" fill="#fff">Brivane Solar</text>
  </svg>

  <div class="benefit left abs" style="top:2472px;left:126px;width:250px;">
    <h4>COST</h4>
    <p>Solar panels are now more affordable, &amp; tax incentives and rebates are available nationally and locally</p>
  </div>
  <div class="benefit left abs" style="top:2613px;left:50px;width:254px;">
    <h4>EFFICIENCY</h4>
    <p>Solar panels are becoming more efficient, generating a surplus of electricity for your home.</p>
  </div>
  <div class="benefit left abs" style="top:2776px;left:96px;width:250px;">
    <h4>LOW MAINTENANCE</h4>
    <p>Solar panels require little maintenance, making them a perfect power-generating option.</p>
  </div>
  <div class="benefit abs" style="top:2472px;left:822px;width:266px;">
    <h4>ENVIRONMENTAL IMPACT</h4>
    <p>Solar panels have a minimal environmental impact, and reduce carbon footprint making them a perfect green option.</p>
  </div>
  <div class="benefit abs" style="top:2616px;left:885px;width:240px;">
    <h4>SAVINGS</h4>
    <p>Utility companies are raising costs on customers annually by 4%-10%</p>
  </div>
  <div class="benefit abs" style="top:2767px;left:858px;width:280px;">
    <h4>HOME VALUE</h4>
    <p>Installing solar panels increases the value of your home by at least 4% according to recent studies</p>
  </div>
</section>

<section>
  <svg class="abs" style="top:2937px;left:0" width="1200" height="625" viewBox="0 0 1200 625">
    <defs><linearGradient id="aboutBg" x1="0" y1="0" x2="1" y2="1"><stop offset="0" stop-color="#2e927f"/><stop offset="1" stop-color="#25857b"/></linearGradient>
    <radialGradient id="rays"><stop offset=".55" stop-color="#e3b94c" stop-opacity="0"/><stop offset=".7" stop-color="#e3b94c" stop-opacity=".55"/><stop offset="1" stop-color="#d9473a" stop-opacity="0"/></radialGradient></defs>
    <rect width="1200" height="625" fill="url(#aboutBg)"/>
    <polygon points="0,0 1200,0 600,117" fill="#fff"/>
    <circle cx="393" cy="375" r="300" fill="url(#rays)" role="img" aria-label="Sunburst rays behind the team photo"/>
    <circle cx="393" cy="375" r="200" fill="#223e49"/>
  </svg>
  <div class="abs" role="img" aria-label="Team of six staff members in navy company shirts standing outdoors on a residential street" style="top:3119px;left:198px;width:390px;height:390px;border-radius:50%;background:linear-gradient(180deg,#dfe9f1 0%,#b7c9d4 45%,#3c5e8c 65%,#8a8f86 100%);"></div>
  <h2 class="about-title">ABOUT US</h2>
  <div class="about-rule"></div>
  <div class="about-copy">
    <p>Brivane: a derivative of the Latin word Socius (noun); partner, ally At Brivane Solar, we believe that solid partnerships are the building blocks behind every success story. By approaching every aspect of our business model with transparency and integrity, we have built a foundation of industry-leading experts and lifelong clients.</p>
    <p>Our approach is simple: we listen, educate and collaborate. Brivane is dedicated to offering our partners the highest-level of non-bias industry education so they are empowered to make the right decision based on their needs, not ours.</p>
  </div>
  <div class="btn" style="top:3436px;left:650px;width:159px;height:52px;background:var(--gold);">READ MORE</div>
</section>

<section>
  <h2 class="section-title" style="top:3628px;">LATEST <em>BLOG</em></h2>
  <div class="abs" style="top:3677px;left:579px;width:42px;height:3px;background:var(--teal)"></div>

  <article class="blog-card" style="left:112px;">
    <div class="blog-img" role="img" aria-label="Man working at a desk with a laptop in a bright office" style="background:linear-gradient(135deg,#c9b9a3,#7b6b5a 55%,#e8e4dc);"></div>
    <div class="blog-date">02 APR 2022</div>
    <h3>Now You Can Blog from<br>Everywhere!</h3>
    <p>We've made it quick and convenient for you to manage your blog from anywhere. Here are some great ways you can post to your...</p>
  </article>
  <article class="blog-card" style="left:445px;">
    <div class="blog-img" role="img" aria-label="Blue sea and island coastline seen over white terrace rooftops" style="background:linear-gradient(180deg,#bcd6ee 0%,#2f6fb4 35%,#1b4f94 60%,#eef2f5 85%);"></div>
    <div class="blog-date">02 APR 2022</div>
    <h3>Design a Stunning<br>Blog</h3>
    <p>When it comes to design, the Pagefold blog has everything you need to create beautiful posts that will grab your reader's attention.</p>
  </article>
  <article class="blog-card" style="left:777px;">
    <div class="blog-img" role="img" aria-label="Green potted plants and glass vases on a table" style="background:linear-gradient(135deg,#f1f3ee,#86a86a 45%,#2f8a86 75%,#e9ede8);"></div>
    <div class="blog-date">02 APR 2022</div>
    <h3>Grow Your Blog<br>Community</h3>
    <p>With Pagefold Blog, you're not only sharing your voice with the world, you can also build an active online community.</p>
  </article>
</section>

<footer>
  <svg class="abs" style="top:4140px;left:0" width="1200" height="504" viewBox="0 0 1200 504">
    <polygon points="0,98 423,18 1200,96 1200,504 0,504" fill="#2b8c7e"/>
    <polygon points="0,112 423,32 1200,110 1200,504 0,504" fill="#213f4b"/>
  </svg>

  <div class="brand" style="top:4302px;left:112px;font-size:28px;color:#fff;">
    <span class="brand-dot" style="width:18px;height:18px;"></span>Brivane Solar
  </div>
  <p class="footer-about">At Brivane Solar, believe partnerships are the building blocks behind every success story. By approaching every aspect of our business model with transparency and integrity.</p>

  <div class="footer-head" style="left:389px;">CONTACT INFO</div>
  <div class="contact-item" style="top:4336px;">
    <svg width="20" height="24" viewBox="0 0 24 28" fill="none" stroke="#fff" stroke-width="2"><path d="M12 26s9-9 9-15a9 9 0 0 0-18 0c0 6 9 15 9 15z"/><circle cx="12" cy="11" r="3"/></svg>
    <h5>ADDRESS</h5>
    <p>48 Palmetto Avenue, Suite 210<br>Lakemere, Florida 32000</p>
  </div>
  <div class="contact-item" style="top:4425px;">
    <svg width="22" height="22" viewBox="0 0 24 24" fill="none" stroke="#fff" stroke-width="1.8"><path d="M5 3h4l2 5-2.5 1.5a11 11 0 0 0 6 6L16 13l5 2v4a2 2 0 0 1-2 2A17 17 0 0 1 3 5a2 2 0 0 1 2-2z"/></svg>
    <h5>PHONE</h5>
    <p>(555.014.2290)</p>
  </div>
  <div class="contact-item" style="top:4490px;">
    <svg width="22" height="18" viewBox="0 0 24 18" fill="none" stroke="#fff" stroke-width="1.8"><rect x="1" y="1" width="22" height="16"/><path d="M1 1l11 9 11-9"/></svg>
    <h5>EMAIL</h5>
    <p>hello@brivanesolar-example.com</p>
  </div>

  <div class="footer-head" style="left:629px;">RECENT POSTS</div>
  <div class="post" style="top:4344px;">
    <div class="thumb" role="img" aria-label="Two-storey house with solar panels" style="background:linear-gradient(180deg,#9fb8d0,#6f7d70 60%,#4f6b3d);"></div>
    <div><p>Sed ut perspiciatis unde</p><small><svg width="13" height="13" viewBox="0 0 24 24" fill="none" stroke="#fff" stroke-width="3"><circle cx="12" cy="12" r="10"/><path d="M12 6v6l4 2"/></svg>21 Mar 2014</small></div>
  </div>
  <div class="post" style="top:4445px;">
    <div class="thumb" role="img" aria-label="Roof covered in solar panels under blue sky" style="background:linear-gradient(180deg,#4a86c5,#2b4d7a 55%,#c7a66a);"></div>
    <div><p>Sed ut perspiciatis unde</p><small><svg width="13" height="13" viewBox="0 0 24 24" fill="none" stroke="#fff" stroke-width="3"><circle cx="12" cy="12" r="10"/><path d="M12 6v6l4 2"/></svg>21 Mar 2014</small></div>
  </div>

  <div class="footer-head" style="left:919px;">RECENT WORKS</div>
  <div class="work" role="img" aria-label="House exterior" style="top:4344px;left:920px;background:linear-gradient(180deg,#a9c0d6,#7b8578 60%,#4f6b3d);"></div>
  <div class="work" role="img" aria-label="House exterior" style="top:4344px;left:1011px;background:linear-gradient(180deg,#b4c8dc,#868f8a 60%,#56703f);"></div>
  <div class="work" role="img" aria-label="House exterior" style="top:4434px;left:920px;background:linear-gradient(180deg,#9fb8d0,#6c786b 60%,#4a6636);"></div>
  <div class="work" role="img" aria-label="House exterior" style="top:4434px;left:1011px;background:linear-gradient(180deg,#b9cde0,#8a928a 60%,#5a7442);"></div>

  <p class="copyright">©2022 Brivane Solar.All rights reserved.</p>
</footer>

</body>
</html>
```